Mobil Battery Sales and Instalation

We are a automotive roadside svc company. I am looking to focus on battery sales and instalation We offer tire changes, lockuot, jump starts fuel delivry and battery sales This design should be battery sales and instalation focused My company name is. Harbor Lane Svcs. 909-512-7364 call or text Hours 7am to 9pm. Free service call and instalation with purchase of new battery. Free testing Free battery disposal Colors we like are black and orange or red and black

Target Market(s)

Automotive, RV, Comerical truck, motorcycle and boat

Industry/Entity Type

Automotive

Requirements
Must have
• Pic of battery
• Mobil battery service.
Nice to have
• I want people to see this card and know its a mobil service for battery sales and installation. But can see we offer other services.
• Use my company name but i dont want that to be the standout. (Tuck it in somewhere).
Should not have
• No pictures of any trucks cars etc.
• we do not tow!

```html
<!DOCTYPE html>
<html lang="en">
<head>
<meta charset="utf-8">
<title>Harbor Lane Svcs – Mobile Battery Service Card</title>
<link rel="stylesheet" href="https://fonts.googleapis.com/css2?family=Questrial&family=Oswald:wght@400&display=swap">
<style>
  :root {
    --orange: #f26a1b;
    --orange-light: #f7931e;
    --red: #e3141b;
    --ink: #2b2b2b;
    --text-grey: #333333;
    --card-white: #ffffff;
    --panel-grey: #ececec;
    --page-bg: #f2f2f2;
  }
  html, body {
    margin: 0;
    padding: 0;
    width: 1125px;
    height: 1200px;
    overflow: hidden;
    background: var(--page-bg);
  }
  .card {
    position: absolute;
    left: 12px;
    top: 230px;
    width: 1101px;
    height: 741px;
    background: var(--card-white);
    overflow: hidden;
    font-family: "Questrial", sans-serif;
    color: var(--text-grey);
    box-shadow: 0 2px 8px rgba(0,0,0,0.15);
  }
  .card-shapes {
    position: absolute;
    inset: 0;
  }
  .brand-name {
    position: absolute;
    left: 63px;
    top: 44px;
    margin: 0;
    font-family: "Questrial", sans-serif;
    font-weight: 400;
    font-size: 58px;
    line-height: 1.1;
    color: var(--orange);
  }
  .service-tagline {
    position: absolute;
    left: 505px;
    top: 34px;
    margin: 0;
    font-family: "Oswald", sans-serif;
    font-size: 26px;
    line-height: 38px;
    color: var(--ink);
  }
  .contact-line {
    position: absolute;
    left: 765px;
    margin: 0;
    color: #fff;
    white-space: nowrap;
  }
  .contact-phone { top: 45px; font-size: 42px; line-height: 50px; }
  .contact-hours { top: 108px; font-size: 30px; line-height: 50px; }
  .markets {
    position: absolute;
    left: 497px;
    top: 205px;
    margin: 0;
    font-family: "Oswald", sans-serif;
    font-size: 39px;
    line-height: 50px;
    color: #fff;
    text-transform: uppercase;
  }
  .best-in-label {
    position: absolute;
    left: 90px;
    top: 236px;
    margin: 0;
    font-size: 30px;
    line-height: 44px;
    color: #fff;
  }
  .service-list {
    position: absolute;
    left: 66px;
    top: 314px;
    margin: 0;
    padding: 0;
    list-style: none;
    font-size: 30px;
  }
  .service-list li {
    display: flex;
    align-items: center;
    height: 44px;
    white-space: nowrap;
  }
  .service-list svg { width: 25px; height: 25px; margin-right: 14px; flex: none; }
  .offer {
    position: absolute;
    left: 66px;
    top: 556px;
    margin: 0;
    font-size: 28px;
    line-height: 36px;
    color: var(--red);
  }
  .free-extras {
    position: absolute;
    left: 66px;
    top: 681px;
    margin: 0;
    font-size: 28px;
    line-height: 50px;
    color: #fff;
  }
  .battery-photo {
    position: absolute;
    left: 505px;
    top: 338px;
    width: 530px;
    height: 395px;
  }
</style>
</head>
<body>
  <main class="card">
    <svg class="card-shapes" width="1101" height="741" viewBox="0 0 1101 741" aria-hidden="true">
      <defs>
        <linearGradient id="panelGrey" x1="0" y1="0" x2="0" y2="1">
          <stop offset="0" stop-color="#ffffff"/>
          <stop offset="1" stop-color="#e4e4e4"/>
        </linearGradient>
        <linearGradient id="bandOrange" x1="0" y1="0" x2="1" y2="0">
          <stop offset="0" stop-color="#ee4a1c"/>
          <stop offset="1" stop-color="#f7931e"/>
        </linearGradient>
      </defs>
      <!-- right panel background -->
      <path d="M470 0 H1101 V741 H420 Q440 420 370 310 Q470 170 470 0 Z" fill="url(#panelGrey)"/>
      <!-- swoosh -->
      <path d="M415 0 H483 Q500 170 370 310 Q450 160 415 0 Z" fill="var(--red)"/>
      <path d="M445 0 H490 Q500 180 380 310 Q470 170 445 0 Z" fill="var(--orange)"/>
      <!-- market band -->
      <path d="M370 310 Q420 260 462 195 H1101 V310 Z" fill="url(#bandOrange)"/>
      <!-- contact bars -->
      <rect x="723" y="45" width="378" height="50" fill="var(--orange)"/>
      <rect x="723" y="108" width="378" height="50" fill="var(--orange)"/>
      <circle cx="720" cy="70" r="27" fill="#fff"/>
      <circle cx="720" cy="70" r="23" fill="var(--red)"/>
      <path d="M710 58 l6 -2 l4 9 l-4 3 q3 7 9 10 l3 -4 l9 4 l-2 6 q-15 3 -25 -26 z" fill="#fff"/>
      <circle cx="720" cy="133" r="27" fill="#fff"/>
      <circle cx="720" cy="133" r="23" fill="var(--red)"/>
      <rect x="708" y="122" width="24" height="17" rx="4" fill="none" stroke="#fff" stroke-width="2.5"/>
      <path d="M713 139 l-2 7 l7 -7" fill="#fff"/>
      <line x1="713" y1="128" x2="727" y2="128" stroke="#fff" stroke-width="2"/>
      <line x1="713" y1="133" x2="724" y2="133" stroke="#fff" stroke-width="2"/>
      <!-- best-in ribbon -->
      <path d="M82 232 H351 L333 288 H66 Z" fill="var(--red)"/>
      <path d="M66 288 L82 232 L70 232 Z" fill="#a80e12"/>
      <path d="M96 288 L104 300 L112 288 Z" fill="#a80e12"/>
      <!-- bottom offer bar -->
      <path d="M0 681 H610 L651 731 H0 Z" fill="url(#bandOrange)"/>
    </svg>

    <h1 class="brand-name">Harbor Lane<br>Svcs.</h1>

    <p class="service-tagline">Mobil Service For<br>Battery Sales<br>And Installation</p>
    <p class="contact-line contact-phone">909-512-7364</p>
    <p class="contact-line contact-hours">or text 7am to 9pm</p>

    <p class="markets">For Auto, Commercial,<br>Marine/RV,Powersport</p>

    <p class="best-in-label">We are Best in</p>
    <ul class="service-list">
      <li><svg viewBox="0 0 24 24"><circle cx="12" cy="12" r="10" fill="none" stroke="#f26a1b" stroke-width="2"/><path d="M7 12 l4 4 l8 -9" fill="none" stroke="#f26a1b" stroke-width="2.5"/></svg>Battery Sales</li>
      <li><svg viewBox="0 0 24 24"><circle cx="12" cy="12" r="10" fill="none" stroke="#f26a1b" stroke-width="2"/><path d="M7 12 l4 4 l8 -9" fill="none" stroke="#f26a1b" stroke-width="2.5"/></svg>Battery installation</li>
      <li><svg viewBox="0 0 24 24"><circle cx="12" cy="12" r="10" fill="none" stroke="#f26a1b" stroke-width="2"/><path d="M7 12 l4 4 l8 -9" fill="none" stroke="#f26a1b" stroke-width="2.5"/></svg>Tire Changes</li>
      <li><svg viewBox="0 0 24 24"><circle cx="12" cy="12" r="10" fill="none" stroke="#f26a1b" stroke-width="2"/><path d="M7 12 l4 4 l8 -9" fill="none" stroke="#f26a1b" stroke-width="2.5"/></svg>Lockout</li>
      <li><svg viewBox="0 0 24 24"><circle cx="12" cy="12" r="10" fill="none" stroke="#f26a1b" stroke-width="2"/><path d="M7 12 l4 4 l8 -9" fill="none" stroke="#f26a1b" stroke-width="2.5"/></svg>Jump Starts Fuel Delivery</li>
    </ul>

    <p class="offer">Free Service Call And<br>Installation With Purchase<br>Of New Battery.</p>
    <p class="free-extras">Free Testing Free Battery Disposal</p>

    <svg class="battery-photo" role="img" aria-label="Photo of three vehicle batteries with black lids and red and blue terminals" viewBox="0 0 530 395">
      <defs>
        <linearGradient id="batteryTone" x1="0" y1="0" x2="0" y2="1">
          <stop offset="0" stop-color="#3a3a3a"/>
          <stop offset="0.35" stop-color="#9a9a9a"/>
          <stop offset="1" stop-color="#e6e6e6"/>
        </linearGradient>
      </defs>
      <rect x="0" y="0" width="530" height="395" rx="18" fill="url(#batteryTone)" opacity="0.85"/>
    </svg>
  </main>
</body>
</html>
```